Business Card Design Project

Doctor, Pain Management. Need a new business card design with appointment info on the back. New address is 18 Birchwood Court, Suite 304, Holloway, NJ 07519. Right now I believe the rest of the information is staying the same.

```html
<!DOCTYPE html>
<html lang="en">
<head>
<meta charset="utf-8">
<title>Steadfast Pain Management – Business Card</title>
<link href="https://fonts.googleapis.com/css2?family=Gelasio:wght@400;700&display=swap" rel="stylesheet">
<style>
  :root {
    --page-bg: #d9d9d7;
    --front-bg-top: #3f3f33;
    --front-bg-bottom: #2f2f27;
    --placeholder-tone: #48463a;
    --accent-yellow: #f2ec4e;
    --front-text: #ffffff;
    --back-bg: #fbfbfa;
    --back-text: #3a3a36;
    --back-rule: #4a4a44;
  }
  * { box-sizing: border-box; margin: 0; padding: 0; }
  html, body { width: 1200px; height: 864px; overflow: hidden; }
  body {
    background: var(--page-bg);
    font-family: "Gelasio", Georgia, serif;
    display: flex;
    align-items: center;
    justify-content: center;
    gap: 40px;
  }
  .card {
    width: 540px;
    height: 309px;
    position: relative;
    box-shadow: 0 6px 18px rgba(0,0,0,0.18);
  }

  /* Front */
  .card-front {
    background: linear-gradient(160deg, var(--front-bg-top), var(--front-bg-bottom));
    color: var(--front-text);
    text-align: center;
    padding-top: 20px;
  }
  .illustration-area {
    position: absolute;
    left: 205px;
    top: 80px;
    width: 130px;
    height: 229px;
    background: var(--placeholder-tone);
  }
  .front-content { position: relative; z-index: 1; }
  .practice-name {
    color: var(--accent-yellow);
    font-weight: 700;
    font-size: 33px;
    letter-spacing: 0.5px;
    line-height: 1.15;
  }
  .doctor-name {
    font-weight: 700;
    font-size: 21px;
    margin-top: 10px;
    line-height: 1.2;
  }
  .credentials {
    color: var(--accent-yellow);
    font-size: 14px;
    margin-top: 2px;
  }
  .contact-list {
    list-style: none;
    font-size: 19px;
    line-height: 1.2;
    margin-top: 10px;
  }
  .address { font-size: 18px; }

  /* Back */
  .card-back {
    background: var(--back-bg);
    color: var(--back-text);
    padding: 18px 28px 20px;
    display: flex;
    flex-direction: column;
    justify-content: space-between;
  }
  .appointment-title {
    text-align: center;
    font-size: 28px;
    font-weight: 400;
    line-height: 1.1;
  }
  .appointment-note {
    text-align: center;
    font-size: 16px;
    line-height: 1.2;
  }
  .field-row {
    display: flex;
    align-items: flex-end;
    font-size: 16px;
    gap: 4px;
  }
  .field-line {
    flex: 1;
    border-bottom: 1px solid var(--back-rule);
    height: 14px;
  }
  .field-gap { width: 24px; }
  .day-list {
    list-style: none;
    display: flex;
    justify-content: space-between;
    font-size: 18px;
  }
  .day-list li { display: flex; align-items: center; gap: 4px; }
  .day-box { width: 14px; height: 14px; border: 1px solid var(--back-text); }
  .back-footer {
    display: flex;
    justify-content: space-between;
    align-items: flex-end;
    font-size: 14px;
    line-height: 1.3;
  }
  .back-footer .web { text-align: right; font-size: 15px; }
</style>
</head>
<body>
  <section class="card card-front">
    <div class="illustration-area" role="img" aria-label="Anatomical illustration of a human back and spine"></div>
    <div class="front-content">
      <h1 class="practice-name">Steadfast Pain Management</h1>
      <p class="doctor-name">Dr. Meilin Zhou</p>
      <p class="credentials">M.D., Ph.D.</p>
      <ul class="contact-list">
        <li>(973) 555-0148</li>
        <li>(973) 555.0162</li>
        <li>www.steadfastpm.com</li>
        <li>steadfastpmc.service@mailhub.com</li>
        <li class="address">18 Birchwood Court, Suite 304, Holloway, NJ 07519</li>
      </ul>
    </div>
  </section>

  <section class="card card-back">
    <h2 class="appointment-title">Appoinment</h2>
    <p class="appointment-note">If you are unable to keep your appoinment,<br>please contact us as soon as posible.</p>
    <div class="field-row"><span>For:</span><span class="field-line"></span></div>
    <div class="field-row"><span>Date:</span><span class="field-line"></span><span class="field-gap"></span><span>Time:</span><span class="field-line"></span></div>
    <ul class="day-list">
      <li><span class="day-box"></span>Mon</li>
      <li><span class="day-box"></span>Tue</li>
      <li><span class="day-box"></span>Wed</li>
      <li><span class="day-box"></span>Thu</li>
      <li><span class="day-box"></span>Fri</li>
      <li><span class="day-box"></span>Sat</li>
      <li><span class="day-box"></span>Sun</li>
    </ul>
    <div class="back-footer">
      <div class="phones">(973) 555-0148<br>(973) 555.0162</div>
      <div class="web">www.steadfastpm.com<br>steadfastpmc.service@mailhub.com</div>
    </div>
  </section>
</body>
</html>
```